Grins of Maplecrest - Dental, needs a redesign

Purpose:
Redesign website: http://www.grinsofmaplecrest.example/

Sections are important, but for content, we can use existing website or have some placeholder text to fill in later.

Some of the required sections:
About us, contact us, services, our offices, our staff, patient education, patient forms (link to Molvaro can be used here), link to friendwall, testimonials

Editability:
We would like to be able to update and edit the content in the future, for small changes

Pictures:
Here is a link to the staff pictures we’d like to use on the website:
https://www.filecrate.example/sh/503k7pq2vv884x9/BBDPyrTe_wKQj7ZumfXKTgghb?dl=0
You don't have to use all the pictures; just a few.

Friendwall page:
https://www.friendwall.example/Grins-of-Maplecrest-527163048915276

Colors: Calming colors/images for a soothing feeling... to assure the patient that it'll not be that bad.

Target Market(s)

General population

Industry/Entity Type

Dental Clinic

Coding

Coded - Design and coding required

Number of Pages Required

5+ page

Requirements
Must have
• About us, contact us, services, our offices, our staff, patient education, patient forms (link to Molvaro can be used here), link to friendwall, testimonials.
• Just create the placeholders for content or use from existing website.
• The staff picture of everyone needs to be on the home page - because that makes it more personal and has received positive feedback from many patients.

```html
<!DOCTYPE html>
<html lang="en">
<head>
<meta charset="utf-8">
<title>Dr. Anjali Verma, DDS – Grins of Maplecrest</title>
<link rel="stylesheet" href="https://fonts.googleapis.com/css2?family=Raleway:wght@300;400;500;600&family=Kaushan+Script&display=swap">
<style>
:root{
  --teal:#3cc3d3;
  --purple:#9c72d4;
  --pink:#e52f8f;
  --navy:#2d3a63;
  --ink:#333;
  --text:#5a5a5a;
  --line:#cfd3d8;
  --soft:#eef1f4;
  --lavender:#ece4f6;
  --footer:#2a2a2a;
}
*{box-sizing:border-box;margin:0;padding:0}
html,body{width:1200px;height:4235px;overflow:hidden}
body{font-family:"Raleway",sans-serif;color:var(--text);background:#fff;position:relative}
section,header,footer{position:relative;width:1200px;overflow:hidden}
.band-line{height:3px;background:linear-gradient(90deg,var(--purple),var(--teal))}

/* header */
.site-header{height:112px;display:flex;align-items:center;justify-content:space-between;padding:0 76px 0 80px}
.brand{display:flex;align-items:center;gap:14px;color:var(--navy);font-weight:600;font-size:21px;line-height:1.25}
.brand-dot{width:52px;height:52px;border-radius:50%;background:var(--teal)}
.main-nav{display:flex;gap:14px;font-size:15px}
.main-nav a{color:var(--ink);text-decoration:none}
.main-nav a.active{color:var(--teal)}

/* hero */
.hero{height:565px;background:linear-gradient(90deg,#fff 0%,#f7f4fb 40%,#efe8f6 100%)}
.hero-photo{position:absolute;right:0;top:0;width:660px;height:100%;
  background:
    radial-gradient(ellipse 34% 42% at 58% 52%,rgba(226,176,150,.95) 0%,rgba(214,160,132,.75) 45%,rgba(214,160,132,0) 100%),
    radial-gradient(ellipse 48% 70% at 66% 45%,rgba(92,52,36,.85) 0%,rgba(92,52,36,.45) 55%,rgba(92,52,36,0) 100%),
    linear-gradient(90deg,rgba(247,244,251,1) 0%,rgba(239,232,246,0) 30%,rgba(239,232,246,0) 85%,#f2eef6 100%);}
.hero-title{position:absolute;left:80px;top:190px;font-family:"Kaushan Script",cursive;font-weight:400;line-height:1.2}
.hero-title .line1{font-size:56px;color:#111;display:block}
.hero-title .line2{font-size:64px;color:var(--pink);display:block}

/* section heading */
.section-title{text-align:center;font-size:36px;font-weight:400;color:var(--ink);padding-top:34px}
.divider{display:flex;align-items:center;justify-content:center;gap:10px;margin:14px auto 0}
.divider span{display:block;height:3px;width:270px;background:var(--line)}
.divider i{display:block;width:14px;height:14px;border-radius:50%;border:3px solid var(--teal)}
.divider.wide span{width:470px;height:2px}

/* intro */
.intro{height:515px;background:linear-gradient(180deg,#fff 0%,#fff 58%,var(--lavender) 100%)}
.intro-copy{width:1060px;margin:30px auto 0;text-align:center;font-size:12.5px;line-height:1.7}
.intro-copy p{margin-bottom:14px}
.group-photo{position:absolute;left:200px;bottom:0;width:800px;height:215px;
  background:
    radial-gradient(ellipse 14% 38% at 12% 42%,rgba(222,178,150,.9),rgba(222,178,150,0)),
    radial-gradient(ellipse 14% 38% at 30% 55%,rgba(204,160,132,.9),rgba(204,160,132,0)),
    radial-gradient(ellipse 14% 38% at 50% 40%,rgba(226,184,156,.9),rgba(226,184,156,0)),
    radial-gradient(ellipse 14% 38% at 70% 50%,rgba(214,168,140,.9),rgba(214,168,140,0)),
    radial-gradient(ellipse 14% 38% at 90% 38%,rgba(226,180,150,.9),rgba(226,180,150,0)),
    linear-gradient(180deg,rgba(255,255,255,0) 0%,rgba(236,226,240,.6) 100%);}
.intro::after{content:"";position:absolute;left:0;bottom:0;width:100%;height:3px;background:linear-gradient(90deg,var(--purple),var(--teal))}

/* services */
.services{height:750px}
.service-grid{display:grid;grid-template-columns:repeat(4,230px);column-gap:36px;row-gap:34px;justify-content:center;margin-top:46px}
.service{text-align:center}
.service-icon{width:104px;height:104px;border-radius:50%;border:2px solid #aaa;margin:0 auto 18px;display:flex;align-items:center;justify-content:center}
.service h3{font-size:19px;font-weight:500;color:var(--ink);margin-bottom:8px}
.service p{font-size:11.5px;line-height:1.5}

/* gallery */
.gallery{height:678px;border-top:3px solid transparent;border-image:linear-gradient(90deg,var(--purple),var(--teal)) 1}
.gallery-grid{display:grid;grid-template-columns:repeat(3,345px);grid-template-rows:repeat(2,226px);gap:6px;justify-content:center;margin-top:34px}
.t1{background:radial-gradient(circle at 30% 55%,#5a4236 0%,rgba(90,66,54,0) 30%),linear-gradient(135deg,#e4dccf 0%,#b8aa96 55%,#4e4540 100%)}
.t2{background:radial-gradient(circle at 55% 45%,#c99a82 0%,rgba(201,154,130,0) 25%),linear-gradient(135deg,#d8c09a 0%,#8c6e52 50%,#2e2621 100%)}
.t3{background:linear-gradient(180deg,#d7e6f2 0%,#c5d8ea 28%,#8b5a44 40%,#7a4c3a 62%,#8e9a6a 75%,#6f8a4a 100%)}
.t4{background:linear-gradient(135deg,#f3f2ee 0%,#d8dcd6 45%,#8fa6a1 80%,#3d4a4a 100%)}
.t5{background:linear-gradient(180deg,#b48b66 0%,#8a6446 45%,#5a3e2c 75%,#3a2a20 100%)}
.t6{background:linear-gradient(160deg,#2f6a4c 0%,#2f6a4c 60%,#6f8e60 80%,#9ab07e 100%)}

/* team */
.team{height:494px;border-top:3px solid transparent;border-image:linear-gradient(90deg,var(--purple),var(--teal)) 1}
.team-row{display:flex;justify-content:center;gap:28px;margin-top:40px}
.member{width:236px;height:228px;border:1px solid #ddd;padding:6px;position:relative;background:#fff}
.member-photo{width:100%;height:100%;
  background:
    radial-gradient(ellipse 24% 22% at 50% 36%,#c99a7e 0%,rgba(201,154,126,0) 100%),
    radial-gradient(ellipse 32% 30% at 50% 30%,#3a2a24 0%,rgba(58,42,36,0) 100%),
    linear-gradient(180deg,#f4f4f4 0%,#ececec 55%,#2a2a2a 78%,#1e1e1e 100%);}
.member-label{position:absolute;left:6px;right:6px;bottom:6px;background:rgba(40,40,40,.8);text-align:center;padding:5px 0}
.member-label strong{display:block;color:#fff;font-weight:500;font-size:14px}
.member-label em{font-style:normal;color:var(--teal);font-size:11px}
.carousel-arrow{position:absolute;top:296px}
.carousel-arrow.prev{left:26px}
.carousel-arrow.next{right:26px}

/* testimonials */
.testimonials{height:415px;border-top:3px solid transparent;border-image:linear-gradient(90deg,var(--purple),var(--teal)) 1}
.quote-row{display:flex;justify-content:center;gap:50px;margin-top:36px}
.quote-card{width:494px;height:134px;border:2px solid #444;border-radius:4px;padding:16px 130px 0 56px;position:relative;font-size:11px;line-height:1.55}
.quote-mark{position:absolute;left:14px;top:-4px;font-size:70px;color:#bfe9ef;font-family:Georgia,serif}
.quote-author{margin-top:6px;font-size:10px;color:var(--ink)}
.quote-author b{display:block;color:var(--teal);font-weight:500}
.quote-face{position:absolute;right:16px;bottom:-42px;width:106px;height:106px;border-radius:50%;border:3px solid #c8202a;background:radial-gradient(circle at 50% 45%,#d9ad92 0%,#b98b73 40%,#e9e9e9 75%)}

/* contact */
.contact{height:641px;background:var(--soft);border-top:3px solid transparent;border-image:linear-gradient(90deg,var(--purple),var(--teal)) 1}
.contact-cols{display:flex;margin-top:40px;padding:0 79px}
.contact-info{width:486px;font-size:13px;color:var(--ink);line-height:1.35}
.contact-info .label{margin-top:12px}
.contact-info .big{font-size:28px;color:var(--teal);margin-top:2px}
.contact-info .mid{font-size:20px;color:var(--teal)}
.hours div{color:var(--pink)}
.hours div span{color:var(--purple)}
.contact-form{border-left:1px solid #d5d9de;padding-left:48px;width:560px}
.field{display:flex;align-items:center;margin-bottom:24px}
.field label{width:93px;font-size:13px;color:var(--ink)}
.field .input{width:412px;height:42px;border:1px solid #ccc;background:#fff;font-size:13px;color:#aaa;padding:12px}
.field .input.tall{height:74px}
.send-btn{margin-left:93px;width:140px;height:42px;background:var(--teal);color:#fff;border:none;font-family:inherit;font-size:17px}

/* footer */
.site-footer{height:65px;background:var(--footer);color:#ccc;font-size:12px;padding:12px 80px;display:flex;justify-content:space-between;align-items:flex-start}
.footer-nav a{color:#ddd;text-decoration:none;margin-right:8px}
.footer-copy{margin-top:6px;font-size:10px;color:#999}
.footer-right{display:flex;align-items:center;gap:14px;margin-top:8px}
.footer-right a{color:#ddd;text-decoration:none}
.social{display:flex;align-items:center;gap:6px;color:#ddd}
.social i{display:block;width:18px;height:18px;background:#3b5a9a}
</style>
</head>
<body>

<header class="site-header">
  <div class="brand"><span class="brand-dot"></span><span>Dr. Anjali Verma, DDS<br>Grins of Maplecrest</span></div>
  <nav class="main-nav">
    <a class="active" href="#">Home</a><a href="#">About</a><a href="#">Services</a><a href="#">Patient Education</a><a href="#">Patient Form</a><a href="#">Testimonial</a><a href="#">Contact</a>
  </nav>
</header>
<div class="band-line"></div>

<section class="hero">
  <div class="hero-photo" role="img" aria-label="Photo of a smiling woman with dark hair"></div>
  <h1 class="hero-title"><span class="line1">Live The Life With</span><span class="line2">Great Smile</span></h1>
</section>
<div class="band-line"></div>

<section class="intro">
  <h2 class="section-title">Honestly Caring &amp; Quality Dentistry</h2>
  <div class="divider wide"><span></span><span></span></div>
  <div class="intro-copy">
    <p>Dr. Anjali Verma provides a full range of dental services to the whole family. Many of our patient families span multiple generations. Our Team are dedicated to taking the time needed to provide the very best care every patient deserves.</p>
    <p>Please tour our web site to learn more about family dentistry, cosmetic dentistry and our restorative dental services. We invite you to call us with any questions you may have – we look forward to meeting you and your family!</p>
    <p>New patients looking for quality dental care in a relaxed environment are welcome! We accept PPO, Indemnity and Traditional insurance plans.</p>
  </div>
  <div class="group-photo" role="img" aria-label="Photo of a group of smiling young people"></div>
</section>

<section class="services">
  <h2 class="section-title">Our Dental Services</h2>
  <div class="divider"><span></span><i></i><span></span></div>
  <div class="service-grid">
    <div class="service"><div class="service-icon"><svg width="40" height="40"><circle cx="20" cy="20" r="14" fill="none" stroke="#3cc3d3" stroke-width="3"/></svg></div><h3>Fillings</h3><p>Fillings are done to remove decay and replace the affected tooth structure. It is called a filling because new material fills the hole that decay left.</p></div>
    <div class="service"><div class="service-icon"><svg width="40" height="40"><rect x="8" y="8" width="24" height="24" fill="none" stroke="#9c72d4" stroke-width="3"/></svg></div><h3>Gum Treatments</h3><p>The gums, ligaments and bone around the teeth form the foundation for ones teeth. All structures are also referred to as the periodontium.</p></div>
    <div class="service"><div class="service-icon"><svg width="40" height="40"><path d="M6 16 Q20 32 34 16" fill="none" stroke="#3cc3d3" stroke-width="3"/></svg></div><h3>Cosmetic Dentistry</h3><p>This can be anything done to correct imperfections in the appearance of the mouth. Anyone who is unhappy with their smile can have it fixed.</p></div>
    <div class="service"><div class="service-icon"><svg width="40" height="40"><path d="M20 6 V34 M6 20 H34" stroke="#e52f8f" stroke-width="3"/></svg></div><h3>Root Canal Treatment</h3><p>Root canal treatment is made necessary when a cavity is allowed, through neglect, to reach all the way to the pulp.</p></div>
    <div class="service"><div class="service-icon"><svg width="40" height="40"><circle cx="20" cy="20" r="14" fill="none" stroke="#9c72d4" stroke-width="3"/></svg></div><h3>Bonding</h3><p>Bonding involves adhering composite resin material that is matched to the color of the tooth, to the front of the tooth.</p></div>
    <div class="service"><div class="service-icon"><svg width="40" height="40"><path d="M6 14 H34 M6 26 H34" stroke="#3cc3d3" stroke-width="3"/></svg></div><h3>Alignara</h3><p>Alignara straightens your teeth with a series of clear virtually invisible custom-molded aligners.</p></div>
    <div class="service"><div class="service-icon"><svg width="40" height="40"><path d="M20 6 V34" stroke="#3cc3d3" stroke-width="3"/><path d="M12 12 H28 M12 20 H28 M12 28 H28" stroke="#3cc3d3" stroke-width="2"/></svg></div><h3>Implants</h3><p>A dental implant is an option to replace a missing tooth. In this procedure a small titanium shaft is surgically implanted into the bone and allowed to set.</p></div>
    <div class="service"><div class="service-icon"><svg width="40" height="40"><path d="M8 28 L12 12 L20 20 L28 12 L32 28 Z" fill="none" stroke="#9c72d4" stroke-width="3"/></svg></div><h3>Crowns</h3><p>Crowns are full coverage restorations that are used to cover a tooth that is likely to break, or is too broken down to be restored with a filling.</p></div>
  </div>
</section>

<section class="gallery">
  <h2 class="section-title">Our Gallery</h2>
  <div class="divider"><span></span><i></i><span></span></div>
  <div class="gallery-grid">
    <div class="t1" role="img" aria-label="Staff member beside a treatment room monitor"></div>
    <div class="t2" role="img" aria-label="Staff member at the front desk"></div>
    <div class="t3" role="img" aria-label="Brick office building exterior"></div>
    <div class="t4" role="img" aria-label="Treatment room with dental chair"></div>
    <div class="t5" role="img" aria-label="Waiting room with sofa and chairs"></div>
    <div class="t6" role="img" aria-label="Green office sign reading general dentistry"></div>
  </div>
</section>

<section class="team">
  <h2 class="section-title">Our Team</h2>
  <div class="divider"><span></span><i></i><span></span></div>
  <svg class="carousel-arrow prev" width="20" height="34"><path d="M16 2 L4 17 L16 32" fill="none" stroke="#999" stroke-width="3"/></svg>
  <svg class="carousel-arrow next" width="20" height="34"><path d="M4 2 L16 17 L4 32" fill="none" stroke="#999" stroke-width="3"/></svg>
  <div class="team-row">
    <div class="member"><div class="member-photo" role="img" aria-label="Staff portrait"></div><div class="member-label"><strong>Dr. Anjali Verma</strong><em>Dental surgeon</em></div></div>
    <div class="member"><div class="member-photo" role="img" aria-label="Staff portrait"></div><div class="member-label"><strong>Dr. Corinne Hale</strong><em>Dental surgeon</em></div></div>
    <div class="member"><div class="member-photo" role="img" aria-label="Staff portrait"></div><div class="member-label"><strong>Dr. Priya Mehan</strong><em>Dental surgeon</em></div></div>
    <div class="member"><div class="member-photo" role="img" aria-label="Staff portrait"></div><div class="member-label"><strong>Dana Whitlock</strong><em>Dental surgeon</em></div></div>
  </div>
</section>

<section class="testimonials">
  <h2 class="section-title">Our Patient's Testimonial</h2>
  <div class="divider wide"><span></span><span></span></div>
  <div class="quote-row">
    <div class="quote-card"><span class="quote-mark">“</span>The whole team made my visit calm and easy. Every step was explained clearly, the chair was comfortable and I left with a brighter smile than I expected. I am glad to recommend them.<div class="quote-author"><b>Mark Ellison</b>Patient</div><div class="quote-face" role="img" aria-label="Patient portrait"></div></div>
    <div class="quote-card"><span class="quote-mark">“</span>Friendly staff, a relaxed office and gentle care from start to finish. My children now look forward to their checkups, which I never thought I would say. Thank you for everything.<div class="quote-author"><b>Jenna Price</b>Patient</div><div class="quote-face" role="img" aria-label="Patient portrait"></div></div>
  </div>
</section>

<section class="contact">
  <h2 class="section-title">Contact Us</h2>
  <div class="divider"><span></span><i></i><span></span></div>
  <div class="contact-cols">
    <div class="contact-info">
      <div class="label">Call us for any information :</div>
      <div class="big">555-018-2460/2462</div>
      <div class="label">Contact with us :</div>
      <div class="mid">418 Linden Avenue, Suite 2C<br>Maplecrest, IL 60999</div>
      <div class="label">Contact us for your Estimation :</div>
      <div class="mid">info@grinsofmaplecrest.example<br>www.grinsofmaplecrest.example</div>
      <div class="label">Opening Hours :</div>
      <div class="hours">
        <div><span>Monday:</span> 12:00pm to 8:00pm</div>
        <div><span>Tuesday:</span> 10:00am to 7:00pm</div>
        <div><span>Wednesday:</span> Closed</div>
        <div><span>Thursday:</span> 8:00am to 6:00pm</div>
        <div><span>Friday:</span> 8:00am to 5:00pm</div>
        <div><span>Saturday when open:</span> 8:00am to 3:00pm OR 8:00am to 12:00pm</div>
      </div>
    </div>
    <form class="contact-form">
      <div class="field"><label>Name :</label><div class="input">Enter your Name</div></div>
      <div class="field"><label>Email :</label><div class="input">Enter your Email Address</div></div>
      <div class="field"><label>Phone :</label><div class="input">Enter your Phone Number</div></div>
      <div class="field"><label>Address :</label><div class="input">Enter your Address</div></div>
      <div class="field"><label>Message :</label><div class="input tall">Enter your Message</div></div>
      <button class="send-btn" type="button">Send</button>
    </form>
  </div>
</section>

<footer class="site-footer">
  <div>
    <nav class="footer-nav"><a href="#">Home</a>| <a href="#">About</a>| <a href="#">Services</a>| <a href="#">Patient Education</a>| <a href="#">Patient Form</a>| <a href="#">Testimonial</a>| <a href="#">Contact</a></nav>
    <div class="footer-copy">© 2016 grinsofmaplecrest.example . All rights reserved.</div>
  </div>
  <div class="footer-right"><a href="#">Terms &amp; Conditions</a>|<a href="#">Privacy Policy</a><span class="social"><i></i>Friendwall</span></div>
</footer>

</body>
</html>
```